Lip Balm tube design

create label/ product print design for Lip balm tubes
Size of tube
76 mm high
24 mm wide

2.75 x 2" h- this is for the main part of tube, not top cap

Current design has been attached for reference. Would like to stick to something similar but need it to "pop" more and be more readable to user
Designs
Vanilla Mint
Citrus Spice
Coconut Lime
Marshmallow Creme
Satsuma Sugar

Designs must include product information (ingredients) as detailed on examples.
Color palette is color but soft, matte tones

```html
<!DOCTYPE html>
<html lang="en">
<head>
<meta charset="utf-8">
<title>Natural Lip Balm labels</title>
<link href="https://fonts.googleapis.com/css2?family=Italiana&family=Montserrat:wght@400;500;600&family=Parisienne&display=swap" rel="stylesheet">
<style>
  :root{
    --stage:#cfcfcf;
    --divider:#ffffff;
    --citrus-bg:#b85c12; --citrus-ink:#ffffff; --citrus-soft:#e9b07a;
    --vanilla-bg:#d8f2ee; --vanilla-ink:#3e5f58; --vanilla-soft:#9cbcb4;
    --satsuma-bg:#fcd4a8; --satsuma-ink:#d28a3b; --satsuma-soft:#e9b27a;
    --marsh-bg:#efebe3; --marsh-ink:#4a3418; --marsh-soft:#b7a58a;
    --coconut-bg:#e5f2cd; --coconut-ink:#7ea059; --coconut-soft:#b8cf98;
  }
  *{box-sizing:border-box;margin:0;padding:0}
  html,body{width:1200px;height:519px;overflow:hidden}
  body{display:flex;background:var(--divider);gap:4px;font-family:"Montserrat",sans-serif}
  .flavour-panel{flex:1;background:var(--stage);display:flex;justify-content:center;align-items:center;gap:14px}
  .citrus{--bg:var(--citrus-bg);--ink:var(--citrus-ink);--soft:var(--citrus-soft)}
  .vanilla{--bg:var(--vanilla-bg);--ink:var(--vanilla-ink);--soft:var(--vanilla-soft)}
  .satsuma{--bg:var(--satsuma-bg);--ink:var(--satsuma-ink);--soft:var(--satsuma-soft)}
  .marsh{--bg:var(--marsh-bg);--ink:var(--marsh-ink);--soft:var(--marsh-soft)}
  .coconut{--bg:var(--coconut-bg);--ink:var(--coconut-ink);--soft:var(--coconut-soft)}
  .label{position:relative;width:100px;height:318px;background:var(--bg);color:var(--ink)}
  .brand-mark{position:absolute;top:38px;left:0;right:0;display:flex;justify-content:center;align-items:center;gap:3px;font-size:5.5px;font-weight:600;letter-spacing:1px}
  .brand-mark .dot{width:6px;height:6px;border-radius:50%;background:var(--ink)}
  .product-type{position:absolute;top:98px;left:0;right:0;text-align:center;font-size:8.2px;font-weight:500}
  .brand-line{position:absolute;top:110px;left:0;right:0;text-align:center;font-size:4.4px;letter-spacing:1.6px;font-weight:500}
  .botanical{position:absolute;background:var(--soft);opacity:.55;border-radius:40% 60% 50% 50%}
  .label-front .botanical{left:56px;top:126px;width:32px;height:30px}
  .label-back .botanical{left:70px;top:196px;width:22px;height:20px}
  .vertical{position:absolute;writing-mode:vertical-rl;transform:rotate(180deg)}
  .flavour-name{left:10px;top:124px;height:160px;font-family:"Italiana",serif;line-height:.86;white-space:nowrap}
  .flavour-name .word-one{display:block}
  .flavour-name .word-two{display:block;margin-inline-start:58px;font-size:.62em}
  .flavour-name.long-name{font-size:26px}
  .flavour-name.long-name .word-two{font-size:.95em;margin-inline-start:66px}
  .aroma-note{left:58px;top:225px;height:38px;font-size:3.6px;line-height:1.3;text-align:center}
  .cert-badge{position:absolute;left:56px;top:264px;width:20px;height:20px;border-radius:50%;border:1px solid var(--ink)}
  .net-weight{position:absolute;top:300px;left:0;right:0;text-align:center;font-size:4.4px;font-weight:500}
  .back-copy{left:12px;top:120px;height:182px;font-size:3.3px;line-height:1.45}
  .claims{font-family:"Parisienne",cursive;font-size:8.5px;line-height:1.2;display:block}
  .ingredients-title{display:block;font-weight:600;font-size:4.4px;margin-block-start:2px}
  .ingredients{display:block;width:auto}
  .maker{display:block;font-weight:600;margin-block-start:3px}
  .social-row{display:flex;gap:1.5px;margin-block-start:2px}
  .social-row i{display:block;width:4px;height:4px;background:var(--ink);border-radius:1px}
</style>
</head>
<body>

<section class="flavour-panel citrus">
  <article class="label label-front">
    <div class="brand-mark"><span class="dot"></span>SOLENA LEAF</div>
    <p class="product-type">Natural Lip Balm</p>
    <p class="brand-line">SOLENA LEAF</p>
    <div class="botanical" role="img" aria-label="Line drawing of citrus blossoms"></div>
    <h2 class="vertical flavour-name" style="font-size:42px"><span class="word-one">Citrus</span><span class="word-two">Spice</span></h2>
    <p class="vertical aroma-note">Natural Aroma<br>Therapy</p>
    <div class="cert-badge"></div>
    <p class="net-weight">NT WT. 3oz/8.5g</p>
  </article>
  <article class="label label-back">
    <div class="brand-mark"><span class="dot"></span>SOLENA LEAF</div>
    <div class="botanical" role="img" aria-label="Line drawing of citrus blossoms"></div>
    <div class="vertical back-copy">
      <span class="claims">Plant based + Vegan + Cruelty free</span>
      <span class="ingredients-title">Ingredients</span>
      <span class="ingredients">Organic Olive Fruit Oil (Olea Europaea), Organic Coconut Oil (Cocos Nucifera), Organic Shea Butter (Butyrospermum Parkii), Organic Jojoba Seed Oil (Simmondsia Chinensis), Rosehip Seed Oil (Rosa Canina), Vitamin E (Tocopherol), Sunflower Seed Oil (Helianthus Annuus), Vanilla Aroma, Mentha Piperita (Peppermint) Leaf Oil, Dipteryx Odorata (Tonka Bean) Oil</span>
      <span class="maker">SOLENALEAF</span>
      <span class="maker">Made by Solena Leaf, Harlow Creek HC 204</span>
      <span class="social-row"><i></i><i></i><i></i></span>
    </div>
  </article>
</section>

<section class="flavour-panel vanilla">
  <article class="label label-front">
    <div class="brand-mark"><span class="dot"></span>SOLENA LEAF</div>
    <p class="product-type">Natural Lip Balm</p>
    <p class="brand-line">SOLENA LEAF</p>
    <div class="botanical" role="img" aria-label="Line drawing of a mint sprig"></div>
    <h2 class="vertical flavour-name" style="font-size:40px"><span class="word-one">Vanilla</span><span class="word-two">Mint</span></h2>
    <p class="vertical aroma-note">Natural Aroma<br>Therapy</p>
    <div class="cert-badge"></div>
    <p class="net-weight">NT WT. 3oz/8.5g</p>
  </article>
  <article class="label label-back">
    <div class="brand-mark"><span class="dot"></span>SOLENA LEAF</div>
    <div class="botanical" role="img" aria-label="Line drawing of a mint sprig"></div>
    <div class="vertical back-copy">
      <span class="claims">Plant based + Vegan + Cruelty free</span>
      <span class="ingredients-title">Ingredients</span>
      <span class="ingredients">Organic Olive Fruit Oil (Olea Europaea), Organic Coconut Oil (Cocos Nucifera), Organic Shea Butter (Butyrospermum Parkii), Organic Jojoba Seed Oil (Simmondsia Chinensis), Rosehip Seed Oil (Rosa Canina), Vitamin E (Tocopherol), Sunflower Seed Oil (Helianthus Annuus), Vanilla Aroma, Mentha Piperita (Peppermint) Leaf Oil, Dipteryx Odorata (Tonka Bean) Oil</span>
      <span class="maker">SOLENALEAF</span>
      <span class="maker">Made by Solena Leaf, Harlow Creek HC 204</span>
      <span class="social-row"><i></i><i></i><i></i></span>
    </div>
  </article>
</section>

<section class="flavour-panel satsuma">
  <article class="label label-front">
    <div class="brand-mark"><span class="dot"></span>SOLENA LEAF</div>
    <p class="product-type">Natural Lip Balm</p>
    <p class="brand-line">SOLENA LEAF</p>
    <div class="botanical" role="img" aria-label="Line drawing of satsuma blossoms"></div>
    <h2 class="vertical flavour-name" style="font-size:38px"><span class="word-one">Satsuma</span><span class="word-two">Sugar</span></h2>
    <p class="vertical aroma-note">Natural Aroma<br>Therapy</p>
    <div class="cert-badge"></div>
    <p class="net-weight">NT WT. 3oz/8.5g</p>
  </article>
  <article class="label label-back">
    <div class="brand-mark"><span class="dot"></span>SOLENA LEAF</div>
    <div class="botanical" role="img" aria-label="Line drawing of satsuma blossoms"></div>
    <div class="vertical back-copy">
      <span class="claims">Plant based + Vegan + Cruelty free</span>
      <span class="ingredients-title">Ingredients</span>
      <span class="ingredients">Organic Olive Fruit Oil (Olea Europaea), Organic Coconut Oil (Cocos Nucifera), Organic Shea Butter (Butyrospermum Parkii), Organic Jojoba Seed Oil (Simmondsia Chinensis), Rosehip Seed Oil (Rosa Canina), Vitamin E (Tocopherol), Sunflower Seed Oil (Helianthus Annuus), Vanilla Aroma, Mentha Piperita (Peppermint) Leaf Oil, Dipteryx Odorata (Tonka Bean) Oil</span>
      <span class="maker">SOLENALEAF</span>
      <span class="maker">Made by Solena Leaf, Harlow Creek HC 204</span>
      <span class="social-row"><i></i><i></i><i></i></span>
    </div>
  </article>
</section>

<section class="flavour-panel marsh">
  <article class="label label-front">
    <div class="brand-mark"><span class="dot"></span>SOLENA LEAF</div>
    <p class="product-type">Natural Lip Balm</p>
    <p class="brand-line">SOLENA LEAF</p>
    <div class="botanical" role="img" aria-label="Line drawing of a mallow flower"></div>
    <h2 class="vertical flavour-name long-name"><span class="word-one">Marshmallow</span><span class="word-two">Creme</span></h2>
    <p class="vertical aroma-note">Natural Aroma<br>Therapy</p>
    <div class="cert-badge"></div>
    <p class="net-weight">NT WT. 3oz/8.5g</p>
  </article>
  <article class="label label-back">
    <div class="brand-mark"><span class="dot"></span>SOLENA LEAF</div>
    <div class="botanical" role="img" aria-label="Line drawing of a mallow flower"></div>
    <div class="vertical back-copy">
      <span class="claims">Plant based + Vegan + Cruelty free</span>
      <span class="ingredients-title">Ingredients</span>
      <span class="ingredients">Organic Olive Fruit Oil (Olea Europaea), Organic Coconut Oil (Cocos Nucifera), Organic Shea Butter (Butyrospermum Parkii), Organic Jojoba Seed Oil (Simmondsia Chinensis), Rosehip Seed Oil (Rosa Canina), Vitamin E (Tocopherol), Sunflower Seed Oil (Helianthus Annuus), Vanilla Aroma, Mentha Piperita (Peppermint) Leaf Oil, Dipteryx Odorata (Tonka Bean) Oil</span>
      <span class="maker">SOLENALEAF</span>
      <span class="maker">Made by Solena Leaf, Harlow Creek HC 204</span>
      <span class="social-row"><i></i><i></i><i></i></span>
    </div>
  </article>
</section>

<section class="flavour-panel coconut">
  <article class="label label-front">
    <div class="brand-mark"><span class="dot"></span>SOLENA LEAF</div>
    <p class="product-type">Natural Lip Balm</p>
    <p class="brand-line">SOLENA LEAF</p>
    <div class="botanical" role="img" aria-label="Line drawing of a lime leaf sprig"></div>
    <h2 class="vertical flavour-name" style="font-size:40px"><span class="word-one">Coconut</span><span class="word-two">Lime</span></h2>
    <p class="vertical aroma-note">Natural Aroma<br>Therapy</p>
    <div class="cert-badge"></div>
    <p class="net-weight">NT WT. 3oz/8.5g</p>
  </article>
  <article class="label label-back">
    <div class="brand-mark"><span class="dot"></span>SOLENA LEAF</div>
    <div class="botanical" role="img" aria-label="Line drawing of a lime leaf sprig"></div>
    <div class="vertical back-copy">
      <span class="claims">Plant based + Vegan + Cruelty free</span>
      <span class="ingredients-title">Ingredients</span>
      <span class="ingredients">Organic Olive Fruit Oil (Olea Europaea), Organic Coconut Oil (Cocos Nucifera), Organic Shea Butter (Butyrospermum Parkii), Organic Jojoba Seed Oil (Simmondsia Chinensis), Rosehip Seed Oil (Rosa Canina), Vitamin E (Tocopherol), Sunflower Seed Oil (Helianthus Annuus), Vanilla Aroma, Mentha Piperita (Peppermint) Leaf Oil, Dipteryx Odorata (Tonka Bean) Oil</span>
      <span class="maker">SOLENALEAF</span>
      <span class="maker">Made by Solena Leaf, Harlow Creek HC 204</span>
      <span class="social-row"><i></i><i></i><i></i></span>
    </div>
  </article>
</section>

</body>
</html>
```